BUSINESS CARD FOR GUITAR SCHOOL

I would like to design a business card for my Guitar Music School. The school is called "Pluck & Meadow".

The card should be yellow.

Target Market(s)

18-35 years old

Industry/Entity Type

School

Contact Information for Business Card

I would like to design a business card for my Guitar Music School. The school is called "Pluck & Meadow". The card should be yellow.

Card must be consistent with my website design: www.pluckandmeadow.com.sg

Requirements
Must have
• 1) Name of Company
• 2) Company Logo
• 3) Name of Employee
• 4) Position of Employee
• 5) Contact Number
• 6) Address
Nice to have
• Creative Design
• Card must be consistent with my website design: www.pluckandmeadow.com.sg
Should not have
• Boring Design

```html
<!DOCTYPE html>
<html lang="en">
<head>
<meta charset="utf-8">
<title>Pluck &amp; Meadow – Business Card</title>
<link rel="stylesheet" href="https://fonts.googleapis.com/css2?family=Cabin:ital,wght@0,400;0,700;1,400&display=swap">
<style>
  :root {
    --bg: #e9eaec;
    --card-yellow-top: #f4e6ad;
    --card-yellow-bottom: #ecc85c;
    --card-white: #f7f7f7;
    --ink-grey: #8c8c8c;
    --lettering-yellow: #f0cf6a;
    --shadow: rgba(0, 0, 0, 0.16);
  }
  * { box-sizing: border-box; margin: 0; padding: 0; }
  html, body {
    width: 1200px;
    height: 999px;
    overflow: hidden;
    background: var(--bg);
    font-family: "Cabin", "Gill Sans", sans-serif;
  }
  .canvas {
    position: relative;
    width: 1200px;
    height: 999px;
  }
  .card {
    position: absolute;
    width: 700px;
    height: 400px;
    box-shadow: 0 14px 30px var(--shadow);
  }
  .card-front {
    left: 110px;
    top: 70px;
    background: linear-gradient(170deg, var(--card-yellow-top) 0%, var(--card-yellow-bottom) 100%);
    color: var(--ink-grey);
  }
  .brand {
    position: absolute;
    right: 60px;
    top: 62px;
    text-align: right;
  }
  .brand-name {
    font-weight: 700;
    font-size: 58px;
    line-height: 1;
    letter-spacing: -1px;
  }
  .brand-tagline {
    margin-top: 10px;
    font-size: 17px;
    letter-spacing: 0.3px;
  }
  .contact {
    position: absolute;
    left: 56px;
    bottom: 52px;
    line-height: 1.3;
  }
  .employee-name {
    font-weight: 700;
    font-size: 25px;
    letter-spacing: 0.5px;
  }
  .employee-role {
    font-style: italic;
    font-size: 19px;
    margin-bottom: 10px;
  }
  .contact-line {
    font-size: 19px;
    letter-spacing: 0.5px;
  }
  .contact-gap { height: 16px; }
  .card-back {
    left: 400px;
    top: 530px;
    background: var(--card-white);
  }
  .lettering {
    position: absolute;
    left: 230px;
    top: 95px;
    width: 240px;
    height: 210px;
    border-radius: 18px;
    background: var(--lettering-yellow);
    opacity: 0.85;
  }
</style>
</head>
<body>
  <main class="canvas">
    <section class="card card-front" aria-label="Business card front">
      <div class="brand">
        <div class="brand-name">Pluck &amp; Meadow</div>
        <div class="brand-tagline">Growing Players Chord by Chord</div>
      </div>
      <div class="contact">
        <div class="employee-name">&lt;Name of Employee&gt;</div>
        <div class="employee-role">&lt;Position of Employee&gt;</div>
        <div class="contact-line">&lt;Contact Number&gt;</div>
        <div class="contact-gap"></div>
        <div class="contact-line">&lt;Address&gt;</div>
        <div class="contact-line">&lt;Address&gt;</div>
      </div>
    </section>

    <section class="card card-back" aria-label="Business card back">
      <div class="lettering" role="img" aria-label="Hand-lettered yellow brush slogan in three stacked lines"></div>
    </section>
  </main>
</body>
</html>
```